Heating and Air Conditioning Company Needs a Business Card Design

Need a business card design for a company in South Carolina called "Larkfield Heating & Cooling LLC". We install, maintain, and repair HVAC systems and the bulk of our business is residential. We have a logo and are looking for a clean, professional looking card that resonates with "setting the standard for service and comfort".
Updates
Forgot to include this info - Licensed & Insured

Industry/Entity Type
Business

```html
<!DOCTYPE html>
<html lang="en">
<head>
<meta charset="utf-8">
<title>Larkfield Heating &amp; Cooling LLC — Business Card</title>
<link rel="stylesheet" href="https://fonts.googleapis.com/css2?family=Open+Sans:wght@400;600;700;800&display=swap">
<style>
  :root {
    --brand-blue: #0b56b3;
    --text-blue: #1f5fb0;
    --accent-red: #e3202b;
    --ink: #1b1b1b;
    --paper: #ffffff;
    --backdrop: #e9e7e3;
  }
  * { box-sizing: border-box; margin: 0; padding: 0; }
  html, body { width: 1200px; height: 900px; overflow: hidden; }
  body {
    background: var(--backdrop);
    font-family: "Open Sans", Arial, sans-serif;
    display: flex; flex-direction: column; align-items: center; justify-content: center;
    gap: 40px;
  }
  .card {
    width: 660px; height: 377px; position: relative; overflow: hidden;
    box-shadow: 0 6px 18px rgba(0,0,0,.18);
  }
  /* Back side */
  .card-back {
    background: var(--brand-blue); color: var(--paper);
    display: flex; flex-direction: column; align-items: center; justify-content: center;
  }
  .brand { display: flex; align-items: center; gap: 14px; }
  .brand-dot { width: 46px; height: 46px; border-radius: 50%; flex: none; }
  .brand-name { font-weight: 800; letter-spacing: .5px; line-height: 1.1; }
  .card-back .brand-dot { background: var(--paper); }
  .card-back .brand-name { color: var(--paper); font-size: 32px; }
  .services {
    margin-top: 34px; text-align: center; font-size: 20px; letter-spacing: 1.5px; line-height: 1.5;
  }
  /* Front side */
  .card-front { background: var(--paper); }
  .card-front .brand { position: absolute; top: 46px; left: 44px; }
  .card-front .brand-dot { background: var(--text-blue); }
  .card-front .brand-name { color: var(--ink); font-size: 34px; }
  .person { position: absolute; left: 48px; top: 168px; }
  .person-name { color: var(--accent-red); font-weight: 700; font-size: 24px; letter-spacing: .5px; }
  .person-role { color: var(--text-blue); font-weight: 700; font-size: 17px; margin-top: 2px; }
  .person-address { color: var(--text-blue); font-size: 16px; line-height: 1.4; margin-top: 8px; }
  .divider { position: absolute; left: 330px; top: 178px; width: 1px; height: 108px; background: var(--text-blue); }
  .contacts { position: absolute; left: 352px; top: 180px; list-style: none; font-size: 17px; line-height: 1.55; color: var(--text-blue); letter-spacing: .3px; }
  .contacts b { color: var(--accent-red); font-weight: 600; margin-right: 4px; }
  .web-band { position: absolute; left: 0; bottom: 0; width: 560px; height: 50px; }
  .web-text {
    position: absolute; left: 40px; bottom: 12px; color: var(--paper);
    font-size: 17px; letter-spacing: 2.5px; font-weight: 600;
  }
</style>
</head>
<body>
  <section class="card card-back">
    <div class="brand">
      <span class="brand-dot"></span>
      <span class="brand-name">Larkfield Heating &amp; Cooling LLC</span>
    </div>
    <p class="services">Heating • Cooling • Plumbing<br>Residential • Commercial • Industrial</p>
  </section>

  <section class="card card-front">
    <div class="brand">
      <span class="brand-dot"></span>
      <span class="brand-name">Larkfield Heating &amp; Cooling LLC</span>
    </div>
    <div class="person">
      <p class="person-name">Dale Whitmore</p>
      <p class="person-role">Certified Technician</p>
      <p class="person-address">218 Birch Hollow Road,<br>Lakeside, SC 29650</p>
    </div>
    <span class="divider"></span>
    <ul class="contacts">
      <li><b>T:</b>(555) 310-4820</li>
      <li><b>C:</b>(555) 318-2271</li>
      <li><b>F:</b>(555) 310-4839</li>
      <li><b>E:</b>dale@larkfieldhc.net</li>
    </ul>
    <svg class="web-band" viewBox="0 0 560 50" preserveAspectRatio="none" aria-hidden="true">
      <polygon points="0,6 520,6 560,50 0,50" fill="#e3202b"/>
    </svg>
    <p class="web-text">Visit us: www.larkfieldhc.net</p>
  </section>
</body>
</html>
```